Law firm website marketed direct to many individual clients

I need someone to design a very basic website for a law firm that will be very eye catching. It's going to be a single-paged, scrolling website with a small number of folds. I have uploaded a simple word document that outlines the basics of what I thought could be the layout, but I am open to suggestion on font, size, shades of color, organization, etc. etc. Essentially the website just needs to be a very efficient and visually appealing way of conveying some simple messages.

Target Market(s)

High volumes of individuals who have gotten into a car accident and then google on their phones a lawyer to hire to represent them.

Industry/Entity Type

Legal

Number of Pages Required

1 page

Font styles to use
Serif
Sans Serif

Colors
34a7d7
85cae6
0592cd

Requirements
Must have
• Must be bright and grab the users attention with color scheme and layout. The different sections should be done in such a way that they can fit entirely onto one smart phone or tablet screen.
Nice to have
• I'd like to try and see what it looks like if in the middle somewhere there is a fold that says "MEET YOUR ATTORNEYS" and includes individual photos of two attorneys, one on the left side and one on the right. And then a small bio section on them. I don't want the photos to include a square or rectangle background, I want the person in the photo to be superimposed on top of whatever pattern or background you have in the fold.
Should not have
• Do not want too much text. Anything more than 2 sentences in any single place is unacceptable.

```html
<!DOCTYPE html>
<html lang="en">
<head>
<meta charset="utf-8">
<title>Harborline Law Group</title>
<link href="https://fonts.googleapis.com/css2?family=Cinzel:wght@400;500&family=Lato:wght@400;700&display=swap" rel="stylesheet">
<style>
:root{
  --blue:#1e95cf;
  --blue-light:#34a7d7;
  --blue-deep:#0592cd;
  --ink:#222;
  --muted:#555;
  --footer:#383c47;
  --footer-bar:#2d3039;
  --white:#fff;
  --serif:'Cinzel',serif;
  --sans:'Lato',sans-serif;
}
*{margin:0;padding:0;box-sizing:border-box}
html,body{width:792px;height:1200px;overflow:hidden}
body{position:relative;background:var(--white);font-family:var(--sans);color:var(--ink)}
.abs{position:absolute}

/* header */
.site-header{left:0;top:0;width:792px;height:53px;background:var(--white);border-bottom:2px solid var(--blue)}
.brand{left:66px;top:16px;display:flex;align-items:center;gap:8px}
.brand-mark{width:20px;height:20px;background:var(--blue)}
.brand-name{font-family:var(--serif);font-size:17px;color:var(--blue);letter-spacing:.5px}
.header-phone{left:590px;top:12px;display:flex;align-items:center;gap:6px}
.header-phone small{display:block;font-size:7px;color:var(--blue);letter-spacing:.3px}
.header-phone strong{display:block;font-family:var(--serif);font-weight:400;font-size:17px;color:#333;line-height:1}

/* hero */
.hero{left:0;top:53px;width:792px;height:309px;background:linear-gradient(100deg,#2c221b 0%,#4a3a2c 35%,#3a3a40 60%,#5a5a60 100%)}
.hero-shade{left:0;top:53px;width:792px;height:309px;background:rgba(0,0,0,.28)}
.hero-kicker{left:0;top:155px;width:792px;text-align:center;color:var(--white);font-size:13px;font-weight:700}
.hero-title{left:0;top:175px;width:792px;text-align:center;color:var(--white);font-family:var(--serif);font-size:31px;letter-spacing:.5px}
.hero-cta{left:332px;top:230px;width:130px;height:25px;background:var(--blue);color:var(--white);display:flex;align-items:center;justify-content:center;gap:6px;font-size:8px;font-weight:700}
.hero-cta span{font-family:var(--serif);font-weight:400;font-size:9px}
.page-dots{left:0;top:197px;width:13px;height:34px;background:#777;display:flex;flex-direction:column;justify-content:space-around;align-items:center;padding:4px 0}
.page-dots i{width:2px;height:2px;background:#fff;border-radius:50%}

/* features */
.feature{width:170px;text-align:center}
.feature-icon{width:68px;height:68px;border-radius:50%;background:linear-gradient(#fdfdfd,#e4e4e4);border:1px solid #ccc;margin:0 auto;display:flex;align-items:center;justify-content:center;box-shadow:0 10px 6px -8px rgba(0,0,0,.15)}
.feature h3{font-family:var(--serif);font-weight:400;color:var(--blue-light);font-size:10px;line-height:12px;margin-top:14px;height:24px;display:flex;align-items:center;justify-content:center}
.feature p{font-size:8px;line-height:9px;margin-top:6px;color:#222}

/* cta band */
.cta-band{left:0;top:588px;width:792px;height:72px;background:var(--blue)}
.cta-band-label{left:66px;top:612px;height:30px;border-left:2px solid var(--white);padding-left:10px;color:var(--white);font-size:17px;font-weight:700;display:flex;align-items:center;letter-spacing:.2px}
.cta-band-phone{left:452px;top:605px;display:flex;align-items:center;gap:18px;color:var(--white);font-family:var(--serif);font-size:30px}

/* panels */
.panel{top:660px;width:396px;height:232px}
.panel-left{left:0;background:linear-gradient(120deg,#2a2420,#4a3a30 50%,#3a2e28)}
.panel-right{left:396px;background:linear-gradient(120deg,#c8c2bc,#a8a6a8 50%,#d6d4d4)}
.panel-shade{top:660px;width:396px;height:232px}
.panel-left-shade{left:0;background:rgba(0,0,0,.25)}
.panel-right-shade{left:396px;background:rgba(255,255,255,.35)}
.panel-frame{top:732px;width:311px;height:98px;border:1px dashed rgba(255,255,255,.55);text-align:center}
.panel-frame.dark{border-color:rgba(60,60,60,.5)}
.panel-frame h2{font-family:var(--serif);font-weight:400;font-size:15px;letter-spacing:.5px;margin-top:-9px;display:inline-block;padding:0 12px}
.panel-frame .rule{width:26px;height:2px;margin:9px auto 11px}
.panel-frame p{font-size:8px;line-height:16px}
.panel-left-frame{left:65px;color:var(--white)}
.panel-left-frame .rule{background:var(--white)}
.panel-right-frame{left:416px;color:#222}
.panel-right-frame .rule{background:var(--blue)}

/* call now */
.callnow{left:66px;top:930px;border-left:2px solid #222;padding-left:11px;height:33px}
.callnow h2{font-family:var(--serif);font-weight:400;font-size:18px;line-height:18px;letter-spacing:.5px}
.callnow p{font-size:8px;margin-top:4px}
.callnow-phone{left:502px;top:928px;width:224px;height:40px;border-top:1px solid #ddd;border-bottom:1px solid #ddd;display:flex;align-items:center;gap:12px;padding-left:22px;font-family:var(--serif);font-size:21px;color:#222}

/* footer */
.site-footer{left:0;top:1000px;width:792px;height:165px;background:var(--footer)}
.contact{left:74px;top:1038px;color:var(--white)}
.contact h2{font-family:var(--serif);font-weight:400;font-size:16px;letter-spacing:.5px;margin-bottom:8px}
.contact-row{display:flex;gap:10px;font-size:9px;line-height:13.5px;margin-bottom:5px}
.contact-row svg{flex:none;margin-top:1px}
.contact-row b{font-weight:700}
.map{left:337px;top:1033px;width:323px;height:98px;border:2px solid #fff;border-radius:3px;background:linear-gradient(135deg,#a8d8ec,#d8e8d4 45%,#f1efe6 60%,#a8d8ec)}
.map-link{left:339px;top:1137px;color:var(--white);font-size:8px;display:flex;align-items:center;gap:5px}
.footer-bar{left:0;top:1165px;width:792px;height:35px;background:var(--footer-bar);color:#ddd;font-size:9px;display:flex;align-items:center;justify-content:center;gap:4px}
.footer-bar b{color:var(--white)}
</style>
</head>
<body>

<header class="site-header abs"></header>
<div class="brand abs"><span class="brand-mark"></span><span class="brand-name">HARBORLINE LAW GROUP</span></div>
<div class="header-phone abs">
  <svg width="26" height="26" viewBox="0 0 26 26"><circle cx="13" cy="13" r="11.5" fill="none" stroke="#222" stroke-width="2"/><path d="M9 8.5c.8-.6 1.5-.5 2 .3l.9 1.6c.3.6.2 1-.3 1.4l-.6.4c.5 1.3 1.4 2.3 2.7 2.9l.5-.6c.4-.5.9-.5 1.4-.2l1.6 1c.7.5.7 1.2.1 1.9-1 1.1-2.4 1.1-4.4-.2-1.8-1.2-3.2-2.9-3.9-4.8-.5-1.5-.4-2.6 0-3.7z" fill="#222"/></svg>
  <div><small>CALL US NOW!</small><strong>555-204-7781</strong></div>
</div>

<section>
  <div class="hero abs" role="img" aria-label="Lawyer in a suit signing documents at a desk with law books behind"></div>
  <div class="hero-shade abs"></div>
  <div class="page-dots abs"><i></i><i></i><i></i></div>
  <p class="hero-kicker abs">ACCIDENT? INJURED?</p>
  <h1 class="hero-title abs">YOUR CASE YOUR MONEY</h1>
  <div class="hero-cta abs">
    <svg width="16" height="16" viewBox="0 0 26 26"><circle cx="13" cy="13" r="11" fill="none" stroke="#fff" stroke-width="2"/><path d="M9 8.5c.8-.6 1.5-.5 2 .3l.9 1.6c.3.6.2 1-.3 1.4l-.6.4c.5 1.3 1.4 2.3 2.7 2.9l.5-.6c.4-.5.9-.5 1.4-.2l1.6 1c.7.5.7 1.2.1 1.9-1 1.1-2.4 1.1-4.4-.2-1.8-1.2-3.2-2.9-3.9-4.8-.5-1.5-.4-2.6 0-3.7z" fill="#fff"/></svg>
    CALL: <span>555-204-7781</span>
  </div>
  <svg class="abs" style="left:387px;top:323px" width="12" height="27" viewBox="0 0 12 27"><rect x="2" y="1" width="8" height="13" rx="4" fill="none" stroke="#fff" stroke-width="1"/><line x1="6" y1="4" x2="6" y2="7" stroke="#fff"/><path d="M2 17l4 3 4-3M2 21l4 3 4-3" fill="none" stroke="#fff" stroke-width="1"/></svg>
</section>

<section>
  <div class="feature abs" style="left:35px;top:411px">
    <div class="feature-icon"><svg width="38" height="28" viewBox="0 0 38 28"><rect x="3" y="5" width="32" height="18" rx="2" fill="#222" transform="rotate(-10 19 14)"/><rect x="7" y="8" width="24" height="12" rx="1" fill="none" stroke="#eee" stroke-width="1.2" transform="rotate(-10 19 14)"/><circle cx="19" cy="14" r="4" fill="#eee"/></svg></div>
    <h3>LOW FEES</h3>
    <p>We charge less, so you<br>keep more.</p>
  </div>
  <div class="feature abs" style="left:197px;top:411px">
    <div class="feature-icon"><svg width="32" height="30" viewBox="0 0 32 30"><circle cx="8" cy="5" r="3" fill="#222"/><circle cx="16" cy="5" r="3" fill="#222"/><circle cx="24" cy="5" r="3" fill="#222"/><rect x="4" y="10" width="24" height="6" fill="#222"/><rect x="6" y="16" width="4" height="12" fill="#222"/><rect x="14" y="16" width="4" height="12" fill="#222"/><rect x="22" y="16" width="4" height="12" fill="#222"/></svg></div>
    <h3>FREE<br>CONSULTATION</h3>
    <p>It's always free to talk<br>to us.</p>
  </div>
  <div class="feature abs" style="left:377px;top:411px">
    <div class="feature-icon"><svg width="30" height="34" viewBox="0 0 30 34"><circle cx="14" cy="12" r="10" fill="none" stroke="#222" stroke-width="2.5"/><circle cx="14" cy="12" r="5" fill="none" stroke="#222" stroke-width="2.5"/><path d="M12 12h4v8l6 2v10H12l-4-8 4-1z" fill="#222"/></svg></div>
    <h3>GET STARTED USING ONLY<br>YOUR PHONE</h3>
    <p>No need to come to the office,<br>sign up using your phone.</p>
  </div>
  <div class="feature abs" style="left:575px;top:411px">
    <div class="feature-icon"><svg width="34" height="32" viewBox="0 0 34 32"><rect x="17" y="2" width="15" height="10" rx="1" fill="none" stroke="#222" stroke-width="1.5"/><path d="M20 12l-2 4 5-4" fill="#222"/><circle cx="13" cy="12" r="5" fill="#222"/><path d="M3 30c0-8 4-12 10-12s10 4 10 12z" fill="#222"/></svg></div>
    <h3>SPEAK DIRECTLY<br>TO A LAWYER</h3>
    <p>No staff screening. Talk right<br>to a lawyer on your first call.</p>
  </div>
</section>

<section>
  <div class="cta-band abs"></div>
  <p class="cta-band-label abs">CALL &nbsp;NOW &nbsp;FOR FREE CONSULTATION &nbsp;:</p>
  <div class="cta-band-phone abs">
    <svg width="36" height="36" viewBox="0 0 26 26"><circle cx="13" cy="13" r="11.5" fill="none" stroke="#fff" stroke-width="1.6"/><path d="M9 8.5c.8-.6 1.5-.5 2 .3l.9 1.6c.3.6.2 1-.3 1.4l-.6.4c.5 1.3 1.4 2.3 2.7 2.9l.5-.6c.4-.5.9-.5 1.4-.2l1.6 1c.7.5.7 1.2.1 1.9-1 1.1-2.4 1.1-4.4-.2-1.8-1.2-3.2-2.9-3.9-4.8-.5-1.5-.4-2.6 0-3.7z" fill="#fff"/></svg>
    555-204-7781
  </div>
</section>

<section>
  <div class="panel panel-left abs" role="img" aria-label="Blurred photo of attorneys talking in a law library"></div>
  <div class="panel-shade panel-left-shade abs"></div>
  <div class="panel panel-right abs" role="img" aria-label="Blurred photo of a lawyer meeting clients at a table"></div>
  <div class="panel-shade panel-right-shade abs"></div>
  <div class="panel-frame panel-left-frame abs">
    <h2>NO FEE UNLESS WE WIN</h2>
    <div class="rule"></div>
    <p>We don't get paid unless you get paid. It's as simple<br>as that. We let our results do the<br>talking for us.</p>
  </div>
  <div class="panel-frame panel-right-frame dark abs">
    <h2>QUESTIONS ABOUT ANYTHING?</h2>
    <div class="rule"></div>
    <p>We're here to help. Feel free to call us at 555-204-7781 to speak to one<br>of our attorneys. With extensive experience in helping clients get the<br>results that they want, our team is always just a phone call away.</p>
  </div>
</section>

<section>
  <div class="callnow abs">
    <h2>CALL US &nbsp;NOW!</h2>
    <p>Lorem ipsum dolor sit amet, consectetuer adipiscing elit, sed diam nonummy nibh</p>
  </div>
  <svg class="abs" style="left:434px;top:942px" width="40" height="16" viewBox="0 0 40 16"><path d="M2 10c10 3 22 2 34-6" fill="none" stroke="#222" stroke-width="1"/><path d="M28 4l8 0-3 7" fill="none" stroke="#222" stroke-width="1"/></svg>
  <div class="callnow-phone abs">
    <svg width="30" height="30" viewBox="0 0 26 26"><circle cx="13" cy="13" r="11.5" fill="none" stroke="#222" stroke-width="1.6"/><path d="M9 8.5c.8-.6 1.5-.5 2 .3l.9 1.6c.3.6.2 1-.3 1.4l-.6.4c.5 1.3 1.4 2.3 2.7 2.9l.5-.6c.4-.5.9-.5 1.4-.2l1.6 1c.7.5.7 1.2.1 1.9-1 1.1-2.4 1.1-4.4-.2-1.8-1.2-3.2-2.9-3.9-4.8-.5-1.5-.4-2.6 0-3.7z" fill="#222"/></svg>
    555-204-7781
  </div>
</section>

<footer>
  <div class="site-footer abs"></div>
  <div class="contact abs">
    <h2>CONTACT INFO</h2>
    <div class="contact-row"><svg width="9" height="13" viewBox="0 0 9 13"><path d="M4.5 0A4.5 4.5 0 0 0 0 4.5C0 8 4.5 13 4.5 13S9 8 9 4.5A4.5 4.5 0 0 0 4.5 0z" fill="#fff"/><circle cx="4.5" cy="4.5" r="1.7" fill="#383c47"/></svg><div><b>Harborline Law Group</b><br>Placeholder Suite 4<br>Riverton, LA 70112</div></div>
    <div class="contact-row"><svg width="11" height="11" viewBox="0 0 26 26"><path d="M4 2c2-1.5 3.6-1.2 4.8.8l2.2 3.8c.7 1.4.5 2.4-.7 3.4l-1.4 1c1.2 3 3.3 5.4 6.4 6.9l1.2-1.5c1-1.2 2.1-1.2 3.4-.4l3.8 2.4c1.7 1.2 1.7 2.8.2 4.5-2.4 2.6-5.6 2.6-10.4-.5C9.2 19.5 5.9 15.5 4.2 11 3 7.4 3.2 4.8 4 2z" fill="#fff"/></svg><b>555-204-7781</b></div>
    <div class="contact-row"><svg width="11" height="9" viewBox="0 0 11 9"><rect x="0" y="0" width="11" height="9" fill="#fff"/><path d="M0 0l5.5 5L11 0" fill="none" stroke="#383c47" stroke-width="1"/></svg><span>info@harborlinelaw.com</span></div>
  </div>
  <div class="map abs" role="img" aria-label="Street map showing the office location by the waterfront"></div>
  <div class="map-link abs">View Full Map <svg width="10" height="6" viewBox="0 0 10 6"><path d="M0 3h9M6 0l3 3-3 3" fill="none" stroke="#fff" stroke-width="1"/></svg></div>
  <div class="footer-bar abs">Copyright © 2016 <b>Harborline Law Group</b> I All Rights Reserved.</div>
</footer>

</body>
</html>
```